New business card for UK roofing company

We are Brindmore Roofing and we need a business card design for our staff.

We offer the following services:

- New roofs
- General roof repairs
- Drone surveys
- Single ply roofing
- Steel cladding
- Asbestos removal
- Electronic leak detection

I have attached our logo. I have also attached example branding printed to our vans. The business card should fit in with the style of our branding.

The business card should have the following information;

Address:
Unit 17c Wendlecroft Farm
Wendlecroft Lane
Hatchington
CM4 9QD

Telephone: 020 7946 0372
24 Hour: 0800 612 4479

Email: ray@brindmoreroofing.example
Mobile: 07700981234
Name: Ray Tunstead
Website: www.brindmoreroofing.example

The business card will be printed in Spot UV, see here: https://www.kestaprint.example/business-cards/spot-uv/

If you need anymore info, please let me know,

```html
<!DOCTYPE html>
<html lang="en">
<head>
<meta charset="utf-8">
<title>Brindmore Roofing – Business Card</title>
<link href="https://fonts.googleapis.com/css2?family=Questrial&family=Roboto:wght@400;700&display=swap" rel="stylesheet">
<style>
  :root{
    --navy:#0e4a7a;
    --cyan:#05aedb;
    --cyan-soft:#9ddcef;
    --paper:#ffffff;
    --backdrop:#0a7fb0;
  }
  *{box-sizing:border-box;margin:0;padding:0}
  html,body{width:1200px;height:1200px;overflow:hidden}
  body{background:var(--backdrop);position:relative;font-family:'Roboto',sans-serif;color:var(--navy)}
  .card{position:absolute;left:231px;width:732px;height:417px;background:var(--paper);overflow:hidden}
  .card--front{top:132px}
  .card--back{top:581px}

  .wordmark{position:absolute;left:44px;top:52px;display:flex;align-items:center;gap:8px;
    font-family:'Roboto',sans-serif;font-weight:700;font-size:24px;color:var(--navy);letter-spacing:-.3px;white-space:nowrap}
  .wordmark__dot{width:22px;height:22px;border-radius:50%;background:var(--cyan)}

  .person{position:absolute;left:44px;top:110px;font-family:'Questrial',sans-serif;font-size:27px;font-weight:400;
    letter-spacing:1.5px;padding-bottom:4px;border-bottom:1px solid var(--cyan-soft);white-space:nowrap}
  .person__first{color:var(--navy)}
  .person__last{color:var(--cyan);margin-left:10px}

  .contacts{position:absolute;left:44px;top:172px;list-style:none}
  .contacts li{display:flex;align-items:flex-start;height:41.5px;font-size:21.5px;line-height:26px;white-space:nowrap}
  .contacts svg{width:24px;height:24px;margin-right:22px;flex:none;fill:var(--navy)}
  .contacts .address{line-height:24px}

  .accent{position:absolute;right:-60px;top:-40px}

  .service{position:absolute;left:621px;top:316px;width:60px;height:60px;text-align:center}
  .service svg{position:absolute;inset:0}
  .service__hours{position:relative;display:block;font-weight:700;font-size:16px;line-height:18px;padding-top:9px}
  .service__label{position:relative;display:block;font-size:9px;line-height:11px}
  .hotline{position:absolute;left:581px;top:381px;width:140px;text-align:center;font-weight:700;
    font-size:17px;line-height:20px;white-space:nowrap}

  .back-mark{position:absolute;inset:0;display:flex;flex-direction:column;align-items:center;justify-content:center;gap:22px}
  .back-mark__dot{width:80px;height:80px;border-radius:50%;background:var(--cyan)}
  .back-mark__name{font-family:'Roboto',sans-serif;font-weight:700;font-size:58px;color:var(--navy);letter-spacing:-1px;white-space:nowrap}
</style>
</head>
<body>

<section class="card card--front" aria-label="Business card front">
  <div class="wordmark"><span class="wordmark__dot"></span>Brindmore Roofing</div>

  <h1 class="person"><span class="person__first">RAY</span><span class="person__last">TUNSTEAD</span></h1>

  <ul class="contacts">
    <li><svg viewBox="0 0 24 24"><path d="M6.6 10.8a15 15 0 0 0 6.6 6.6l2.2-2.2c.3-.3.7-.4 1-.2 1.1.4 2.3.6 3.6.6.6 0 1 .4 1 1V20c0 .6-.4 1-1 1A17 17 0 0 1 3 4c0-.6.4-1 1-1h3.5c.6 0 1 .4 1 1 0 1.3.2 2.5.6 3.6.1.3 0 .7-.2 1z"/></svg>020 7946 0372</li>
    <li><svg viewBox="0 0 24 24"><path d="M7 1h10a2 2 0 0 1 2 2v18a2 2 0 0 1-2 2H7a2 2 0 0 1-2-2V3a2 2 0 0 1 2-2zm0 2v16h10V3zm5 17.2a.9.9 0 1 0 0 1.8.9.9 0 0 0 0-1.8z"/></svg>077 0098 1234</li>
    <li><svg viewBox="0 0 24 24"><path d="M2 5h20v14H2zm2 2v.5l8 5 8-5V7z"/></svg>ray@brindmoreroofing.example</li>
    <li><svg viewBox="0 0 24 24"><path d="M12 2a10 10 0 1 0 0 20 10 10 0 0 0 0-20zm0 1.6c1 1.3 1.8 3.2 2.1 5.4H9.9c.3-2.2 1.1-4.1 2.1-5.4zM8.3 9H4.1a8.4 8.4 0 0 1 4.9-5c-.4 1.4-.6 3.2-.7 5zm0 1.6c0 1.2.1 2.4.3 3.4H4a8.4 8.4 0 0 1 0-3.4zm1.5 0h4.4c.1 1.1.1 2.3 0 3.4H9.8c-.1-1.1-.1-2.3 0-3.4zm5.9 0h4.3a8.4 8.4 0 0 1 0 3.4h-4.3c.1-1 .2-2.2 0-3.4zm0-1.6c0-1.8-.3-3.6-.7-5a8.4 8.4 0 0 1 4.9 5zM4.1 15.6h4.2c.1 1.8.3 3.5.7 4.8a8.4 8.4 0 0 1-4.9-4.8zm5.8 0h4.2c-.3 2.1-1.1 3.9-2.1 5.2-1-1.3-1.8-3.1-2.1-5.2zm5.8 0h4.2a8.4 8.4 0 0 1-4.9 4.8c.4-1.3.6-3 .7-4.8z"/></svg>www.brindmoreroofing.example</li>
    <li class="address"><svg viewBox="0 0 24 24"><path d="M12 2a7 7 0 0 0-7 7c0 5.3 7 13 7 13s7-7.7 7-13a7 7 0 0 0-7-7zm0 9.5a2.5 2.5 0 1 1 0-5 2.5 2.5 0 0 1 0 5z"/></svg><span>Unit 17c Wendlecroft Farm<br>Wendlecroft Lane Hatchington CM4 9QD</span></li>
  </ul>

  <svg class="accent" width="380" height="380" viewBox="0 0 380 380" role="img" aria-label="Large brand accent circle">
    <circle cx="210" cy="170" r="170" fill="var(--cyan)"/>
    <circle cx="210" cy="170" r="150" fill="var(--navy)"/>
  </svg>

  <div class="service">
    <svg viewBox="0 0 60 60" aria-hidden="true">
      <path d="M30 3a27 27 0 1 0 24 14" fill="none" stroke="var(--cyan-soft)" stroke-width="3"/>
      <path d="M40 1l6 5-8 2z" fill="var(--cyan-soft)"/>
    </svg>
    <span class="service__hours">24</span>
    <span class="service__label">Hour<br>Service</span>
  </div>
  <div class="hotline">0800 612 4479</div>
</section>

<section class="card card--back" aria-label="Business card back">
  <div class="back-mark">
    <span class="back-mark__dot"></span>
    <span class="back-mark__name">Brindmore Roofing</span>
  </div>
</section>

</body>
</html>
```